Business Cards for Law Office of Miriam T. Haskell

I need a business card for my new estate planning law firm. I have attached my logo. I would like a design that is professional but not too formal or stuffy.

Target Market(s)

Professionals (lawyers, doctors, businesswomen) between the age of 30 and 50 who are tech-savvy and educated.

Industry/Entity Type

Lawyer

Contact Information for Business Card

Miriam T. Haskell

582 E. 67th Street
9th Floor
New York, NY 10065

Phone: (855) 407-6218
Direct: (917) 563-0472
Email: Miriam@MiriamTHaskellLaw.example
www.MiriamTHaskellLaw.example

Font styles to use
Other font styles liked:
• Corbel

Requirements
Must have
• On the front:
• Miriam T. Haskell, Esq.
• Owner & Founder
• 582 E. 67th Street
• 9th Floor
• New York, NY 10065
• Phone: (855) 407-6218
• Direct: (917) 563-0472
• Email: miriam@miriamthaskelllaw.example
• www.miriamthaskelllaw.example
• On the back:
• LOGO
Nice to have
• I want it to be professional but not too formal or stuffy. Please choose colors that go with my logo.
Should not have
• I don't want TOO MUCH color. Some color is good, but not too much.

```html
<!DOCTYPE html>
<html lang="en">
<head>
<meta charset="utf-8">
<title>Business Cards – Law Office of Miriam T. Haskell</title>
<link href="https://fonts.googleapis.com/css2?family=Source+Sans+3:wght@400;600;700&display=swap" rel="stylesheet">
<style>
  :root {
    --purple: #6b2a7e;
    --orange: #ef7d22;
    --ink: #1e1e1e;
    --paper: #ffffff;
    --backdrop: #e4e4e6;
  }
  * { margin: 0; padding: 0; box-sizing: border-box; }
  html, body { width: 1200px; height: 907px; overflow: hidden; }
  body {
    background: var(--backdrop);
    font-family: "Source Sans 3", "Corbel", sans-serif;
    color: var(--ink);
    position: relative;
  }
  .card {
    position: absolute;
    width: 560px;
    height: 320px;
    background: var(--paper);
    box-shadow: 0 10px 28px rgba(0,0,0,.22);
    overflow: hidden;
  }
  .card--front { left: 60px; top: 90px; }
  .card--back { left: 580px; top: 490px; }
  .card > svg { position: absolute; inset: 0; }

  .firm-name {
    position: absolute;
    color: var(--purple);
    font-weight: 600;
    text-transform: uppercase;
    letter-spacing: .04em;
    line-height: 1.1;
  }
  .card--front .firm-name { left: 28px; top: 34px; font-size: 22px; }
  .card--back .firm-name { left: 70px; top: 100px; font-size: 30px; }
  .firm-name .mark {
    display: inline-block;
    width: 12px; height: 12px;
    background: var(--orange);
    margin-right: 10px;
    vertical-align: middle;
  }

  .attorney {
    position: absolute;
    right: 24px; top: 28px;
    text-align: right;
  }
  .attorney__name { color: var(--purple); font-weight: 700; font-size: 17px; }
  .attorney__title { color: var(--orange); font-size: 13px; }
  .address {
    position: absolute;
    right: 24px; top: 92px;
    text-align: right;
    font-size: 13px;
    font-style: normal;
    line-height: 1.35;
  }

  .contacts {
    position: absolute;
    left: 26px; top: 218px;
    list-style: none;
    font-size: 14px;
    line-height: 1.3;
  }
  .contacts li { display: flex; align-items: center; gap: 6px; }
  .contacts svg { width: 12px; height: 12px; flex: none; }

  .web-front {
    position: absolute;
    right: 22px; top: 286px;
    color: var(--paper);
    font-size: 14px;
    line-height: 18px;
  }
  .web-back {
    position: absolute;
    left: 250px; top: 258px;
    color: var(--purple);
    font-size: 17px;
    letter-spacing: .03em;
  }
</style>
</head>
<body>

<section class="card card--front" aria-label="Business card front">
  <svg width="560" height="320" viewBox="0 0 560 320" aria-hidden="true">
    <line x1="18" y1="205" x2="545" y2="205" stroke="var(--purple)" stroke-width="1"/>
    <path d="M0,300 L244,300 C260,300 264,270 282,268 L560,268" fill="none" stroke="var(--orange)" stroke-width="4"/>
    <path d="M0,308 L250,308 C268,308 272,278 292,276 L560,276 L560,320 L0,320 Z" fill="var(--purple)"/>
  </svg>

  <div class="firm-name"><span class="mark"></span>Law Office of<br>Miriam T. Haskell</div>

  <div class="attorney">
    <div class="attorney__name">Miriam T. Haskell, Esq.</div>
    <div class="attorney__title">Owner &amp; Founder</div>
  </div>

  <address class="address">
    582 E. 67th Street<br>
    9th Floor, New York, NY 10065
  </address>

  <ul class="contacts">
    <li>
      <svg viewBox="0 0 12 12" aria-hidden="true"><circle cx="6" cy="6" r="6" fill="var(--purple)"/><rect x="4" y="2.5" width="4" height="7" rx="1" fill="#fff"/></svg>
      (855) 407-6218
    </li>
    <li>
      <svg viewBox="0 0 12 12" aria-hidden="true"><circle cx="6" cy="6" r="6" fill="var(--purple)"/><rect x="3" y="3.5" width="6" height="5" rx="1" fill="#fff"/></svg>
      (917) 563-0472
    </li>
    <li>
      <svg viewBox="0 0 12 12" aria-hidden="true"><circle cx="6" cy="6" r="6" fill="var(--purple)"/><rect x="2.8" y="3.8" width="6.4" height="4.4" fill="#fff"/><path d="M2.8,3.8 L6,6.4 L9.2,3.8" fill="none" stroke="var(--purple)" stroke-width=".8"/></svg>
      miriam@miriamthaskelllaw.example
    </li>
  </ul>

  <div class="web-front">www.miriamthaskelllaw.example</div>
</section>

<section class="card card--back" aria-label="Business card back">
  <svg width="560" height="320" viewBox="0 0 560 320" aria-hidden="true">
    <line x1="18" y1="150" x2="18" y2="305" stroke="var(--orange)" stroke-width="2"/>
    <line x1="215" y1="270" x2="242" y2="270" stroke="var(--orange)" stroke-width="2"/>
    <line x1="545" y1="20" x2="545" y2="160" stroke="var(--orange)" stroke-width="2"/>
  </svg>

  <div class="firm-name"><span class="mark"></span>Law Office of<br>Miriam T. Haskell</div>

  <div class="web-back">www.miriamthaskelllaw.example</div>
</section>

</body>
</html>
```